Business card design needed for Pollen Bakes

We need a new business card designed for our business. We create complete DIY cake kits to be delivered Australia Wide.

I would like our logo used (see attached).

Industry/Entity Type

Business

Contact Information for Business Card

Pollen Bakes - Complete DIY Cake Kits
www.pollenbakes.com.au
0472 315 904
sales@pollenbakes.com.au
www.friendwall.com/pollenbakes1

Requirements
Must have
• logo

```html
<!DOCTYPE html>
<html lang="en">
<head>
<meta charset="utf-8">
<title>Pollen Bakes – Business Card</title>
<link href="https://fonts.googleapis.com/css2?family=Josefin+Sans:wght@400;600;700&display=swap" rel="stylesheet">
<style>
  :root {
    --page: #e9e6e2;
    --card: #f4f4f4;
    --red: #d4212f;
    --red-deep: #a8101e;
    --blue: #1f7fc4;
    --cream: #fbf1dc;
    --ink: #4a3833;
    --teal: #5fb3b0;
    --brand: #b5162b;
    --illustration-a: #f3c7d8;
    --illustration-b: #b9dcd6;
  }
  * { margin: 0; padding: 0; box-sizing: border-box; }
  html, body {
    width: 1200px; height: 1000px; overflow: hidden;
    background: var(--page);
    font-family: "Josefin Sans", "Century Gothic", sans-serif;
  }
  .card {
    position: absolute; left: 100px; top: 214px;
    width: 1000px; height: 572px;
    background: var(--card);
    box-shadow: 0 10px 30px rgba(0,0,0,.18);
    overflow: hidden;
  }
  .card-art { position: absolute; inset: 0; }
  .mascot-area {
    position: absolute; left: 110px; top: 24px;
    width: 300px; height: 310px; border-radius: 50%;
    background: radial-gradient(circle at 50% 45%, var(--illustration-a), var(--illustration-b) 75%, rgba(185,220,214,0) 100%);
  }
  .brand-mark {
    position: absolute; left: 40px; top: 368px;
    display: flex; align-items: center; gap: 14px;
  }
  .brand-dot { width: 26px; height: 26px; border-radius: 50%; background: var(--brand); }
  .brand-name { font-size: 56px; font-weight: 700; color: var(--brand); line-height: 1; }
  .brand-tagline {
    position: absolute; left: 92px; top: 444px;
    font-size: 24px; font-weight: 600; color: var(--teal);
  }
  .headline {
    position: absolute; left: 470px; top: 62px; width: 500px;
    text-align: center; color: var(--cream);
  }
  .headline h1 { font-size: 56px; font-weight: 700; letter-spacing: 2px; line-height: 1; }
  .headline p {
    margin-top: 10px; padding-top: 10px;
    border-top: 2px solid var(--cream);
    font-size: 17px; font-weight: 600; letter-spacing: 6px;
  }
  .contact { position: absolute; left: 0; top: 0; }
  .contact-icon { position: absolute; left: 525px; width: 36px; height: 36px; }
  .contact-bar {
    position: absolute; left: 600px; width: 400px;
    background: #fff; color: var(--ink);
    clip-path: polygon(18px 0, 100% 0, 100% 100%, 0 100%);
    display: flex; align-items: center; padding-left: 32px;
    white-space: nowrap;
  }
  .bar-phone { top: 198px; height: 60px; font-size: 44px; font-weight: 700; letter-spacing: 1px; }
  .bar-email { top: 280px; height: 44px; font-size: 22px; font-weight: 700; }
  .bar-social { top: 346px; height: 44px; font-size: 22px; font-weight: 400; }
  .icon-phone { top: 210px; }
  .icon-email { top: 284px; }
  .icon-social { top: 350px; }
  .website {
    position: absolute; left: 620px; top: 420px;
    font-size: 27px; font-weight: 600; color: #fff;
  }
</style>
</head>
<body>
<section class="card">
  <svg class="card-art" viewBox="0 0 1000 572" width="1000" height="572" aria-hidden="true">
    <defs>
      <linearGradient id="redPanel" x1="0" y1="0" x2="1" y2="1">
        <stop offset="0" stop-color="#a8101e"/>
        <stop offset="0.5" stop-color="#d4212f"/>
        <stop offset="1" stop-color="#e02a33"/>
      </linearGradient>
    </defs>
    <path d="M40 0 C300 30 400 300 540 470 C600 540 690 562 800 572 L760 572 C660 560 590 530 530 480 C380 320 290 50 25 6 Z" fill="#1f7fc4"/>
    <path d="M70 0 C330 40 420 320 560 470 C620 535 700 558 800 572 L1000 572 L1000 0 Z" fill="url(#redPanel)"/>
  </svg>

  <div class="mascot-area" role="img" aria-label="Illustrated baker holding a piping bag and a pink-frosted cupcake"></div>

  <div class="brand-mark">
    <span class="brand-dot"></span>
    <span class="brand-name">Pollen Bakes</span>
  </div>
  <div class="brand-tagline">complete DIY cake kits</div>

  <header class="headline">
    <h1>POLLEN BAKES</h1>
    <p>COMPLETE DIY CAKE KITS</p>
  </header>

  <div class="contact">
    <svg class="contact-icon icon-phone" viewBox="0 0 36 36" aria-hidden="true">
      <circle cx="18" cy="18" r="16" fill="none" stroke="#fbf1dc" stroke-width="2.5"/>
      <path d="M12 10 l4 0 l1.5 4 l-2.5 1.5 c1 2.5 3 4.5 5.5 5.5 l1.5 -2.5 l4 1.5 l0 4 c-9 0 -14 -5 -14 -14 z" fill="#fbf1dc"/>
    </svg>
    <div class="contact-bar bar-phone">0472 315 904</div>

    <svg class="contact-icon icon-email" viewBox="0 0 36 36" aria-hidden="true">
      <rect x="4" y="9" width="28" height="19" fill="none" stroke="#fbf1dc" stroke-width="2.5"/>
      <path d="M4 9 L18 20 L32 9" fill="none" stroke="#fbf1dc" stroke-width="2.5"/>
    </svg>
    <div class="contact-bar bar-email">SALES@POLLENBAKES.COM.AU</div>

    <svg class="contact-icon icon-social" viewBox="0 0 36 36" aria-hidden="true">
      <circle cx="18" cy="18" r="15" fill="#fbf1dc"/>
    </svg>
    <div class="contact-bar bar-social">www.friendwall.com/pollenbakes1</div>

    <div class="website">www.pollenbakes.com.au</div>
  </div>
</section>
</body>
</html>
```